Facebook & Instagram Ads for Velvet Drift, the world's first device to improve memory throu...

About Us
Velvet Drift® is a revolutionary bedside device that improves memory while you sleep. Backed by groundbreaking clinical research from the Norbrook State University Halvern, our device uses gentle, rotating scents to enhance memory and brian fog naturally. With zero pills, zero side effects, and zero effort, Velvet Drift offers a new path to better memory. www.velvetdrift-example.com

The Challenge
We are looking for bold, imaginative, and highly shareable static and GIF ad designs for Facebook and Instagram. This isn’t just another health device—it’s a category-defining product. Your job is to help us stop the scroll with creative ad concepts that communicate the elegance, science, and life-changing benefits of Velvet Drift.

What We’re Looking For
Format: Static images + short GIF animations (3–8 seconds)
Platforms: Facebook feed, Instagram feed, Instagram Reels
Style: Modern, aspirational, elegant, clean — with a premium feel
Target Audience: Affluent men and women, ages 50+, health-conscious, looking for ways to support memory and brain health and people concerned or worried that they’re losing their memory and aren’t thinking as quickly or crisply as they want,

Creative Direction
Show Velvet Drift as a premium lifestyle product (not medical or clinical in look).
Think high-end wellness meets cutting-edge science.
Use strong visual hooks: elegant bedside setups, active seniors, subtle cues to scents and sleep, calming colors.
Text overlays should be minimal and impactful.

Tone of Voice (for ad copy in the designs)
Aspirational yet credible
Warm, trustworthy, and empowering
Avoid fear tactics or overpromising

Approved Messaging
✅ Velvet Drift improves memory while you sleep
✅ Clinically backed & drug-free
✅ Simple, effortless nightly use
✅ No RX, no side effects
✅ Elegant bedside design
✅ Improves your mood
✅ Feel Younger
✅ Developed by a top 2% scientist in the world (Caldermoor School of Medicine Study)
✅ 226% memory improvement in seniors
✅ 300% memory improvement in dementia patients

Do NOT Say
❌ Cures Alzheimer’s or dementia
❌ Guaranteed results
❌ Any medical claims beyond memory improvement and cognition support

Deliverables
2+ static ad concepts (1080x1080 + 1080x1920 formats)
1+ short GIF ad concepts (3–8 seconds, loopable)
Layered source files (PSD/AI) preferred

What We’ll Provide You
Our website for reference: www.velvetdrift-example.com
Brand guidelines (logo, colors, fonts)
Approved copy lines and scientific references
Device imagery (with logo placement guidelines)

What We Want to See in Your Work
Unique and scroll-stopping ad ideas (not cookie-cutter templates)
Clever ways to communicate memory improvement + science through visuals
A mix of direct product focus AND lifestyle storytelling

Inspiration
Think of Quillo, Tesvi Band, or Brantel level of sleekness—premium, modern, aspirational.

⚡ Your mission: Help us tell the world about the first device that can improve memory while you sleep—with ads so compelling people can’t scroll past.

```html
<!DOCTYPE html>
<html lang="en">
<head>
<meta charset="utf-8">
<title>Velvet Drift — Social Ads</title>
<link rel="stylesheet" href="https://fonts.googleapis.com/css2?family=Outfit:wght@300;400;500;700;800&display=swap">
<style>
  :root{
    --board:#9a7059;
    --cream:#f3e6d8;
    --cream-deep:#e9d3bf;
    --ink:#3e2a22;
    --accent:#a16f5a;
    --stat:#b4611d;
    --line:#d9a37c;
    --orb-light:#f2a65a;
    --orb-dark:#8a4a17;
    --device:#f1efec;
  }
  *{box-sizing:border-box;margin:0;padding:0}
  html,body{width:1200px;height:1075px;overflow:hidden;background:var(--board);font-family:"Outfit",sans-serif;color:var(--ink)}
  .ad{position:absolute;overflow:hidden;
    background:
      radial-gradient(ellipse 70% 40% at 70% 60%, rgba(214,184,150,.45), transparent 70%),
      linear-gradient(180deg,#f5ebe0 0%,var(--cream) 45%,var(--cream-deep) 100%);
    box-shadow:0 14px 30px rgba(60,30,15,.35)}
  .ad--square{left:64px;top:68px;width:527px;height:528px}
  .ad--story{left:609px;top:68px;width:528px;height:939px}

  .backdrop-word{position:absolute;font-weight:800;color:var(--accent);opacity:.14;letter-spacing:-4px;white-space:nowrap;line-height:1}
  .brand{position:absolute;text-align:center;font-weight:300;color:var(--ink);line-height:1.1;letter-spacing:.12em}
  .headline{position:absolute;font-weight:700;line-height:1;letter-spacing:-.03em;white-space:nowrap}
  .headline span{display:block}
  .headline .accent{color:var(--accent)}

  .device{position:absolute;border-radius:14px 14px 18px 18px;
    background:linear-gradient(100deg,#e4e1dd 0%,var(--device) 30%,#ffffff 60%,#ebe8e4 100%);
    box-shadow:0 20px 30px rgba(110,70,40,.25)}
  .device::after{content:"";position:absolute;left:0;right:0;top:37%;height:3px;background:#d98a5c}
  .orb{position:absolute;border-radius:50%;
    background:radial-gradient(circle at 35% 30%,var(--orb-light),#c9732c 55%,var(--orb-dark))}

  .feature{position:absolute;text-align:center;transform:translateX(-50%);white-space:nowrap;line-height:1.15}
  .feature svg{display:block;margin:0 auto 3px;stroke:var(--accent);fill:none;stroke-width:1.3}
  .feature .title{font-weight:400;color:var(--ink)}
  .feature .sub{font-weight:300;color:var(--ink)}

  .stats{position:absolute;border:1px solid var(--line);border-radius:8px;
    background:linear-gradient(90deg,rgba(236,200,180,.55),rgba(245,225,210,.45))}
  .stat{position:absolute;top:0;line-height:1.1}
  .stat .num{font-weight:500;color:var(--stat);letter-spacing:-.02em}
  .stat .label{font-weight:300;color:var(--ink)}
  .stats .divider{position:absolute;width:1px;background:var(--ink);opacity:.6}
</style>
</head>
<body>

<!-- Square feed ad -->
<section class="ad ad--square">
  <div class="backdrop-word" style="left:10px;top:84px;font-size:150px">Memory</div>
  <div class="brand" style="left:0;width:527px;top:44px;font-size:30px">VELVET<br>DRIFT</div>

  <div class="headline" style="left:263px;top:141px">
    <span style="font-size:48px">IMPROVES</span>
    <span class="accent" style="font-size:46px;margin:2px 0 0 14px">MEMORY</span>
    <span style="font-size:28px;margin-top:6px">WHILE YOU SLEEP</span>
  </div>

  <div class="orb" style="left:14px;top:290px;width:44px;height:64px"></div>
  <div class="device" role="img" aria-label="White Velvet Drift bedside scent device with copper trim" style="left:38px;top:165px;width:216px;height:330px"></div>

  <div class="feature" style="left:301px;top:275px">
    <svg width="20" height="18" viewBox="0 0 20 18"><path d="M7 2h6M8 2v6l-5 8h14l-5-8V2"/></svg>
    <div class="title" style="font-size:15px">Clinically</div>
    <div class="sub" style="font-size:12px">backed &amp;<br>drug-free</div>
  </div>
  <div class="feature" style="left:379px;top:275px">
    <svg width="20" height="18" viewBox="0 0 20 18"><path d="M12 3a7 7 0 1 0 5 10 6 6 0 0 1-5-10z"/></svg>
    <div class="title" style="font-size:15px">Simple,</div>
    <div class="sub" style="font-size:12px">effortless<br>nightly use</div>
  </div>
  <div class="feature" style="left:463px;top:275px">
    <svg width="20" height="18" viewBox="0 0 20 18"><circle cx="10" cy="9" r="7.5"/><path d="M7 6l6 6M13 6l-6 6"/></svg>
    <div class="title" style="font-size:15px">No RX,</div>
    <div class="sub" style="font-size:12px">no side effects</div>
  </div>
  <div class="feature" style="left:301px;top:350px">
    <svg width="22" height="20" viewBox="0 0 22 20"><path d="M8 1l2 6 6 2-6 2-2 6-2-6-6-2 6-2z"/><path d="M17 11l1 3 3 1-3 1-1 3-1-3-3-1 3-1z"/></svg>
    <div class="title" style="font-size:15px">Elegant</div>
    <div class="sub" style="font-size:12px">bedside<br>design</div>
  </div>
  <div class="feature" style="left:379px;top:355px">
    <svg width="34" height="18" viewBox="0 0 34 18"><circle cx="10" cy="9" r="8"/><circle cx="24" cy="9" r="8"/></svg>
    <div class="title" style="font-size:15px">Improves</div>
    <div class="sub" style="font-size:12px">your mood</div>
  </div>
  <div class="feature" style="left:463px;top:355px">
    <svg width="20" height="18" viewBox="0 0 20 18"><path d="M3 8a7 7 0 0 1 12-4l2 2M17 10a7 7 0 0 1-12 4l-2-2"/><path d="M17 2v4h-4M3 16v-4h4"/></svg>
    <div class="title" style="font-size:15px">Feel</div>
    <div class="sub" style="font-size:12px">Younger</div>
  </div>

  <div class="stats" style="left:193px;top:430px;width:290px;height:72px">
    <div class="stat" style="left:14px;top:9px">
      <div class="num" style="font-size:27px">226%</div>
      <div class="label" style="font-size:12px">memory improvement<br>in seniors</div>
    </div>
    <div class="divider" style="left:146px;top:14px;height:46px"></div>
    <div class="stat" style="left:155px;top:9px">
      <div class="num" style="font-size:27px">300%</div>
      <div class="label" style="font-size:12px">memory improvement<br>in dementia patients</div>
    </div>
  </div>
  <div class="orb" style="left:467px;top:434px;width:32px;height:32px"></div>
</section>

<!-- Story format ad -->
<section class="ad ad--story">
  <div class="backdrop-word" style="left:14px;top:175px;font-size:190px">Memory</div>
  <div class="brand" style="left:0;width:528px;top:72px;font-size:44px">VELVET<br>DRIFT</div>

  <div class="headline" style="left:96px;top:229px">
    <span style="font-size:70px">IMPROVES</span>
    <span class="accent" style="font-size:68px;margin:2px 0 0 24px">MEMORY</span>
    <span style="font-size:42px;margin-top:6px">WHILE YOU SLEEP</span>
  </div>

  <div class="orb" style="left:22px;top:590px;width:40px;height:60px"></div>
  <div class="device" role="img" aria-label="White Velvet Drift bedside scent device with copper trim" style="left:40px;top:425px;width:258px;height:385px"></div>

  <div class="feature" style="left:356px;top:455px">
    <svg width="24" height="22" viewBox="0 0 20 18"><path d="M7 2h6M8 2v6l-5 8h14l-5-8V2"/></svg>
    <div class="title" style="font-size:19px">Clinically</div>
    <div class="sub" style="font-size:15px">backed &amp;<br>drug-free</div>
  </div>
  <div class="feature" style="left:453px;top:455px">
    <svg width="24" height="22" viewBox="0 0 20 18"><path d="M12 3a7 7 0 1 0 5 10 6 6 0 0 1-5-10z"/></svg>
    <div class="title" style="font-size:19px">Simple,</div>
    <div class="sub" style="font-size:15px">effortless<br>nightly use</div>
  </div>
  <div class="feature" style="left:356px;top:554px">
    <svg width="26" height="24" viewBox="0 0 22 20"><path d="M8 1l2 6 6 2-6 2-2 6-2-6-6-2 6-2z"/><path d="M17 11l1 3 3 1-3 1-1 3-1-3-3-1 3-1z"/></svg>
    <div class="title" style="font-size:19px">Elegant</div>
    <div class="sub" style="font-size:15px">bedside<br>design</div>
  </div>
  <div class="feature" style="left:453px;top:557px">
    <svg width="40" height="22" viewBox="0 0 34 18"><circle cx="10" cy="9" r="8"/><circle cx="24" cy="9" r="8"/></svg>
    <div class="title" style="font-size:19px">Improves</div>
    <div class="sub" style="font-size:15px">your mood</div>
  </div>
  <div class="feature" style="left:356px;top:654px">
    <svg width="24" height="22" viewBox="0 0 20 18"><circle cx="10" cy="9" r="7.5"/><path d="M7 6l6 6M13 6l-6 6"/></svg>
    <div class="title" style="font-size:19px">No RX,</div>
    <div class="sub" style="font-size:15px">no side effects</div>
  </div>
  <div class="feature" style="left:453px;top:654px">
    <svg width="24" height="22" viewBox="0 0 20 18"><path d="M3 8a7 7 0 0 1 12-4l2 2M17 10a7 7 0 0 1-12 4l-2-2"/><path d="M17 2v4h-4M3 16v-4h4"/></svg>
    <div class="title" style="font-size:19px">Feel</div>
    <div class="sub" style="font-size:15px">Younger</div>
  </div>

  <div class="stats" style="left:51px;top:803px;width:422px;height:104px">
    <div class="stat" style="left:21px;top:14px">
      <div class="num" style="font-size:37px">226%</div>
      <div class="label" style="font-size:17px">memory improvement<br>in seniors</div>
    </div>
    <div class="divider" style="left:213px;top:20px;height:68px"></div>
    <div class="stat" style="left:226px;top:14px">
      <div class="num" style="font-size:37px">300%</div>
      <div class="label" style="font-size:17px">memory improvement<br>in dementia patients</div>
    </div>
  </div>
  <div class="orb" style="left:452px;top:809px;width:46px;height:46px"></div>
</section>

</body>
</html>
```